Business Card Design

I am a florist specialising in weddings. I would like a very modern however elegant and simple design. My arrangement designs can be quite rustic with a vintage feel, so if you are able to reflect this in the card that would be great.
Updates

Thank you everyone for your submissions. I have found some further words for inspiration. I am looking for something more earthy and artisan looking. If possible I would like to use 100% recycled paper - the type that even looks rustic and recycled. I may even opt to use a small logo to emphasis the fact that they are made from recycled paper. I know this is quite different to my original brief but I wasn't quite sure what to expect from your designs. Also, with the logo, I give permission for it to be cropped to remove the 'Floral Designer' text. Please contact me if you need any further assistance. Many thanks Lorna-Jayne Petal & Thread

I would prefer not to have any photgraphs & not too much pink. Thank you!

Industry/Entity Type

Florist

Contact Information for Business Card

Lorna-Jayne Tulk
Floral Designer
0417 635 208
lornajayne@petalandthread.com.au
petalandthread.com.au

Requirements
Must have
• My logo

```html
<!DOCTYPE html>
<html lang="en">
<head>
<meta charset="utf-8">
<title>Petal &amp; Thread — Business Card</title>
<link rel="stylesheet" href="https://fonts.googleapis.com/css2?family=Almendra&family=Cinzel:wght@400&family=Arimo&family=Questrial&display=swap">
<style>
  :root {
    --backdrop: #e8e6e3;
    --paper: #ede3d3;
    --paper-light: #f4ede2;
    --paper-warm: #e2d3bd;
    --paper-fleck: #d8c6ab;
    --rose-dust: #d9b9b0;
    --sage: #b9bfa4;
    --stitch: #a8604f;
    --ink: #2a211b;
    --name-rust: #8a3328;
    --title-terracotta: #a5523f;
    --contact: #3b332c;
    --mark: #9aa384;
  }
  * { margin: 0; padding: 0; box-sizing: border-box; }
  html, body {
    width: 1000px;
    height: 1200px;
    overflow: hidden;
    background: var(--backdrop);
  }
  .canvas {
    position: relative;
    width: 1000px;
    height: 1200px;
  }
  .card {
    position: absolute;
    width: 647px;
    height: 378px;
    background: var(--paper);
    overflow: hidden;
  }
  .card--front { left: 184px; top: 104px; }
  .card--back  { left: 182px; top: 677px; }

  .floral-backdrop {
    position: absolute;
    inset: 0;
    background:
      radial-gradient(circle at 22% 38%, var(--rose-dust) 0, transparent 30%),
      radial-gradient(circle at 72% 62%, var(--rose-dust) 0, transparent 28%),
      radial-gradient(circle at 86% 22%, var(--sage) 0, transparent 22%),
      radial-gradient(circle at 40% 80%, var(--sage) 0, transparent 20%),
      linear-gradient(135deg, var(--paper-light), var(--paper) 50%, var(--paper-warm));
    opacity: 0.55;
  }

  .stitch-line {
    position: absolute;
    left: 13px;
    right: 17px;
    height: 0;
    border-top: 1px dashed var(--stitch);
  }
  .stitch-line--top { top: 19px; }
  .stitch-line--bottom { bottom: 19px; }

  .brand {
    position: absolute;
    left: 0; right: 0;
    top: 166px;
    display: flex;
    justify-content: center;
    align-items: center;
    gap: 14px;
  }
  .brand-mark {
    width: 40px;
    height: 40px;
    border-radius: 50%;
    background: var(--mark);
    flex: none;
  }
  .brand-name {
    font-family: "Almendra", serif;
    font-size: 46px;
    line-height: 1;
    color: var(--ink);
  }
  .front-title {
    position: absolute;
    left: 0; right: 0;
    top: 246px;
    text-align: center;
    font-family: "Almendra", serif;
    font-size: 27px;
    line-height: 1;
    color: var(--ink);
  }

  .holder {
    position: absolute;
    left: 36px;
    top: 62px;
  }
  .holder-name {
    font-family: "Cinzel", serif;
    font-size: 23px;
    letter-spacing: 3.5px;
    color: var(--name-rust);
    line-height: 1;
  }
  .holder-title {
    margin-top: 9px;
    font-family: "Arimo", sans-serif;
    font-size: 14px;
    letter-spacing: 1.5px;
    color: var(--title-terracotta);
    line-height: 1;
  }

  .contact-list {
    position: absolute;
    right: 43px;
    top: 271px;
    list-style: none;
    text-align: right;
    font-family: "Questrial", sans-serif;
    font-size: 12px;
    letter-spacing: 1.7px;
    color: var(--contact);
  }
  .contact-list li { line-height: 1; height: 25px; }
</style>
</head>
<body>
<main class="canvas">

  <section class="card card--front">
    <div class="floral-backdrop" role="img" aria-label="Faded background of rustic garden blooms on recycled paper"></div>
    <div class="stitch-line stitch-line--top"></div>
    <div class="stitch-line stitch-line--bottom"></div>
    <div class="brand">
      <span class="brand-mark"></span>
      <span class="brand-name">Petal &amp; Thread</span>
    </div>
    <div class="front-title">Floral Designer</div>
  </section>

  <section class="card card--back">
    <div class="floral-backdrop" role="img" aria-label="Faded background of a rustic bouquet on recycled paper"></div>
    <div class="stitch-line stitch-line--top"></div>
    <div class="stitch-line stitch-line--bottom"></div>
    <div class="holder">
      <div class="holder-name">LORNA-JAYNE TULK</div>
      <div class="holder-title">Floral Designer</div>
    </div>
    <ul class="contact-list">
      <li>0417 635 208</li>
      <li>lornajayne@petalandthread.com.au</li>
      <li>petalandthread.com.au</li>
    </ul>
  </section>

</main>
</body>
</html>
```